Visitenkarten-Design für aufstrebendes, modernes und innovatives Elektrounternehmen
Zielgruppe
Unsere Firma ist im Bereich Elektro- und Gebäudetechnik angesiedelt.
Zielgruppe sind Privatkunden und Geschäftskunden.
Wir machen alles rund um das Thema Elektrotechnik, Elektroinstallation ....
Aufgabenstellung
Es soll ein ansprechendes modernes Design sein. Gerne auch mit Rückseite.
Wir sind ein junges aufstrebendes modernes und innovatives Unternehmen

```html
<!DOCTYPE html>
<html lang="de">
<head>
<meta charset="utf-8">
<title>volten – Geschäftsausstattung</title>
<link href="https://fonts.googleapis.com/css2?family=Signika:wght@400;600;700&family=Roboto:wght@400;500&display=swap" rel="stylesheet">
<style>
:root{
  --stage:#4b4b4b;
  --paper:#ffffff;
  --teal:#1798ad;
  --olive:#c4b80c;
  --yellow:#f2df36;
  --blue:#1e5fa0;
  --ink:#555555;
  --faint:#f7f6ef;
  --pink:#e0369a;
}
*{box-sizing:border-box;margin:0;padding:0}
html,body{width:1200px;height:1200px;overflow:hidden;background:var(--stage)}
.stage{position:relative;width:1200px;height:1200px;font-family:"Roboto",sans-serif}
.measure{position:absolute;inset:0;pointer-events:none}
.measure-label{position:absolute;color:#fff;font:400 13px "Roboto",sans-serif;white-space:nowrap}
.sheet{position:absolute;background:var(--paper);overflow:hidden;box-shadow:4px 6px 8px rgba(0,0,0,.35)}
.wordmark{font-family:"Signika",sans-serif;font-weight:700;color:var(--ink);line-height:1;letter-spacing:-.5px}
.tagline{font-family:"Signika",sans-serif;font-weight:600;color:var(--teal);letter-spacing:.1px;white-space:nowrap}
.mark-dot{position:absolute;border-radius:50%;background:var(--olive)}
.faint-circle{position:absolute;border-radius:50%;background:var(--faint)}

/* letterhead */
.letterhead{left:105px;top:96px;width:504px;height:712px}
.letterhead .band-top{position:absolute;left:0;top:0;width:100%;height:6px;background:var(--teal)}
.letterhead .band-bottom{position:absolute;left:0;bottom:0;width:100%;height:7px;background:var(--olive)}
.letterhead .contact{position:absolute;left:395px;top:41px;height:70px;border-left:1px solid #999;padding-left:4px;font-size:5.6px;line-height:7px;color:#666}
.letterhead .contact p+p{margin-top:7px}
.window-frame{position:absolute;left:52px;top:110px;width:209px;height:101px}
.window-frame i{position:absolute;width:16px;height:16px;border:1px solid #777}
.window-frame .tl{left:0;top:0;border-right:0;border-bottom:0;border-top-left-radius:6px}
.window-frame .tr{right:0;top:0;border-left:0;border-bottom:0;border-top-right-radius:6px}
.window-frame .bl{left:0;bottom:0;border-right:0;border-top:0;border-bottom-left-radius:6px}
.window-frame .br{right:0;bottom:0;border-left:0;border-top:0;border-bottom-right-radius:6px}
.return-line{position:absolute;left:70px;top:117px;font-size:6.5px;color:#666;white-space:nowrap}
.return-line b{font-family:"Signika",sans-serif;font-weight:700;font-size:9px;color:var(--ink)}
.return-line em{font-style:normal;color:var(--olive);margin:0 3px}
.fold-mark{position:absolute;left:0;width:18px;border-top:1px solid #ccc}

/* envelope */
.envelope{left:566px;top:368px;width:557px;height:280px}
.envelope-flap{position:absolute;left:566px;top:290px;width:557px;height:79px}
.flap-text{position:absolute;left:845px;top:322px;transform:translate(-50%,-50%) rotate(180deg);font-size:6.5px;color:#fff;white-space:nowrap}
.flap-text b{font-family:"Signika",sans-serif;font-weight:700;font-size:9px}
.flap-dot{position:absolute;left:836px;top:335px;width:18px;height:18px;border-radius:50%;background:#fff;border:2px solid var(--teal);box-shadow:0 0 0 1px #fff}
.address-window{position:absolute;left:52px;top:127px;width:228px;height:114px;border:1px solid var(--pink);border-radius:7px;padding:3px}
.address-window span{display:block;width:100%;height:100%;border:1px dashed #777;border-radius:5px}
.web{position:absolute;left:403px;top:232px;font-size:9.5px;color:var(--teal);display:flex;align-items:center;gap:4px;white-space:nowrap}

/* service card */
.card-services{left:107px;top:893px;width:379px;height:245px}
.card-services .bar{position:absolute;left:164px;top:33px;width:215px;height:7px;background:var(--olive)}
.services{position:absolute;left:222px;top:61px;font-family:"Signika",sans-serif}
.services h2{font-weight:600;font-size:11.5px;line-height:13px;color:var(--ink);margin-bottom:5px}
.services li{list-style:none;position:relative;color:var(--teal);font-size:11.5px;line-height:18.6px}
.services li::before{content:"";position:absolute;left:-15px;top:5px;width:9px;height:9px;border-radius:50%;background:var(--olive)}
.welcome{position:absolute;left:0;top:208px;width:100%;height:20px;background:var(--teal);color:#fff;font-family:"Signika",sans-serif;font-weight:600;font-size:11px;letter-spacing:.6px;text-align:center;line-height:20px}

/* contact card */
.card-contact{left:689px;top:895px;width:380px;height:245px}
.card-contact .bar-yellow{position:absolute;left:0;top:33px;width:210px;height:7px;background:var(--yellow)}
.card-contact .bar-blue{position:absolute;left:143px;top:209px;width:237px;height:6px;background:var(--blue)}
.person{position:absolute;left:25px;top:86px;font-family:"Signika",sans-serif}
.person h1{font-weight:400;font-size:17px;color:var(--blue);line-height:18px}
.person p{font-size:8.5px;letter-spacing:1.3px;color:var(--ink)}
.card-contact .details{position:absolute;left:25px;top:167px;font-size:7.6px;line-height:9.5px;color:var(--ink)}
.card-contact .details p+p{margin-top:6px}
</style>
</head>
<body>
<div class="stage">

  <svg class="measure" width="1200" height="1200" viewBox="0 0 1200 1200" aria-hidden="true">
    <g stroke="#fff" stroke-width="1.6" fill="#fff">
      <line x1="110" y1="75" x2="604" y2="75"/>
      <path d="M107 75 l15 -8 l-4 8 l4 8z M607 75 l-15 -8 l4 8 l-4 8z" stroke="none"/>
      <line x1="73" y1="102" x2="73" y2="802"/>
      <path d="M73 99 l-8 15 l8 -4 l8 4z M73 805 l-8 -15 l8 4 l8 -4z" stroke="none"/>
      <line x1="695" y1="876" x2="1064" y2="876"/>
      <path d="M692 876 l15 -8 l-4 8 l4 8z M1067 876 l-15 -8 l4 8 l-4 8z" stroke="none"/>
      <line x1="1093" y1="900" x2="1093" y2="1135"/>
      <path d="M1093 897 l-7 13 l7 -4 l7 4z M1093 1138 l-7 -13 l7 4 l7 -4z" stroke="none"/>
    </g>
    <g stroke="#222" stroke-width="1">
      <line x1="105" y1="50" x2="105" y2="81"/><line x1="609" y1="50" x2="609" y2="81"/>
      <line x1="105" y1="826" x2="105" y2="854"/><line x1="609" y1="826" x2="609" y2="854"/>
      <line x1="59" y1="96" x2="90" y2="96"/><line x1="59" y1="808" x2="90" y2="808"/>
      <line x1="624" y1="96" x2="654" y2="96"/><line x1="624" y1="808" x2="654" y2="808"/>
    </g>
  </svg>
  <span class="measure-label" style="left:329px;top:57px">210 mm.</span>
  <span class="measure-label" style="left:38px;top:434px;transform:rotate(-90deg)">297 mm.</span>
  <span class="measure-label" style="left:832px;top:858px">85 mm.</span>
  <span class="measure-label" style="left:1080px;top:1032px;transform:rotate(90deg)">55 mm.</span>

  <!-- letterhead -->
  <section class="sheet letterhead" aria-label="Briefbogen">
    <div class="band-top"></div>
    <div class="faint-circle" style="left:107px;top:287px;width:290px;height:290px"></div>
    <div class="mark-dot" style="left:50px;top:28px;width:50px;height:50px"></div>
    <div class="wordmark" style="position:absolute;left:106px;top:30px;font-size:36px">volten</div>
    <div class="tagline" style="position:absolute;left:116px;top:66px;font-size:8px">ELEKTRO- &amp; GEBÄUDETECHNIK</div>
    <div class="contact">
      <p>Lukas Brenner<br>Elektrotechnikermeister</p>
      <p>Lindenweg 12<br>86999 Talhausen<br>T 08123 456780<br>info@volten-elektro.de</p>
    </div>
    <div class="window-frame"><i class="tl"></i><i class="tr"></i><i class="bl"></i><i class="br"></i></div>
    <div class="return-line"><b>volten</b><em>•</em>Lindenweg 12<em>•</em>86999 Talhausen</div>
    <div class="fold-mark" style="top:253px"></div>
    <div class="fold-mark" style="top:491px"></div>
    <div class="band-bottom"></div>
  </section>

  <!-- envelope -->
  <svg class="envelope-flap" viewBox="0 0 557 79" aria-hidden="true">
    <path d="M0 79 L23 10 Q27 0 38 0 L519 0 Q530 0 534 10 L557 79 Z" fill="var(--teal)"/>
  </svg>
  <div class="flap-text"><b>volten</b> • Lindenweg 12 • 86999 Talhausen</div>
  <div class="flap-dot"></div>
  <section class="sheet envelope" aria-label="Briefumschlag">
    <div class="faint-circle" style="left:294px;top:2px;width:262px;height:262px"></div>
    <div class="mark-dot" style="left:52px;top:26px;width:49px;height:49px"></div>
    <div class="wordmark" style="position:absolute;left:108px;top:28px;font-size:35px">volten</div>
    <div class="tagline" style="position:absolute;left:118px;top:63px;font-size:8px">ELEKTRO- &amp; GEBÄUDETECHNIK</div>
    <div class="address-window"><span></span></div>
    <div class="web">
      <svg width="11" height="11" viewBox="0 0 12 12" aria-hidden="true"><circle cx="6" cy="6" r="5.3" fill="var(--olive)"/><g fill="none" stroke="#fff" stroke-width=".8"><ellipse cx="6" cy="6" rx="2.4" ry="5.3"/><line x1=".7" y1="6" x2="11.3" y2="6"/><line x1="1.5" y1="3.5" x2="10.5" y2="3.5"/><line x1="1.5" y1="8.5" x2="10.5" y2="8.5"/></g></svg>
      www.volten-elektrotechnik.de
    </div>
    <svg style="position:absolute;left:0;top:266px" width="557" height="14" viewBox="0 0 557 14" aria-hidden="true">
      <polygon points="0,0 349,0 363,14 0,14" fill="var(--olive)"/>
      <polygon points="359,0 557,0 557,14 373,14" fill="var(--teal)"/>
    </svg>
  </section>

  <!-- business card: services -->
  <section class="sheet card-services" aria-label="Visitenkarte Rückseite">
    <div class="wordmark" style="position:absolute;left:22px;top:22px;font-size:29px">volten</div>
    <div class="tagline" style="position:absolute;left:31px;top:49px;font-size:7.5px">ELEKTRO- &amp; GEBÄUDETECHNIK</div>
    <div class="bar"></div>
    <div class="mark-dot" style="left:26px;top:70px;width:120px;height:120px"></div>
    <div class="services">
      <h2>Unsere Leistungen<br>im Überblick:</h2>
      <ul>
        <li>LED</li>
        <li>Beleuchtung</li>
        <li>Sicherheitstechnik</li>
        <li>Videoüberwachung</li>
        <li>Elektroinstallation</li>
      </ul>
    </div>
    <div class="welcome">Willkommen bei volten Lichtkonzept</div>
  </section>

  <!-- business card: contact -->
  <section class="sheet card-contact" aria-label="Visitenkarte Vorderseite">
    <div class="bar-yellow"></div>
    <div class="person">
      <h1>Lukas Brenner</h1>
      <p>Elektrotechnikermeister</p>
    </div>
    <div class="details">
      <p>Lindenweg 12<br>86999 Talhausen</p>
      <p>T 08123 456780<br>info@volten-elektro.de</p>
    </div>
    <div class="mark-dot" style="left:212px;top:53px;width:142px;height:142px"></div>
    <div class="bar-blue"></div>
  </section>

</div>
</body>
</html>
```